Letterhead Design Project

Letterhead for a Consultant Cardiologist in Adelaide Australia. Should be very classy, mature and imposing. I would prefer colours that portray confidence, gentleness and serenity.

The PDF attached is for you to see the details that will be on the letterhead and not the design which is extremely poor!

Target Market(s)

Health professionals especially medical doctors

Industry/Entity Type

Consultant

```html
<!DOCTYPE html>
<html lang="en">
<head>
<meta charset="utf-8">
<title>Letterhead – Dr Adaeze O. Marlowe, Cardiologist</title>
<link rel="stylesheet" href="https://fonts.googleapis.com/css2?family=Source+Sans+3:wght@400;600&display=swap">
<style>
  :root {
    --backdrop: #e9e3e7;
    --paper: #ffffff;
    --plum: #a23a63;
    --stripe: #8f8ca8;
    --name-grey: #6b5a7a;
    --sidebar-text: #f6e9ef;
    --trace-tint: #f7e3e8;
  }
  * { margin: 0; padding: 0; box-sizing: border-box; }
  html, body {
    width: 1200px; height: 1000px; overflow: hidden;
    background: var(--backdrop);
    font-family: "Source Sans 3", "Myriad Pro", sans-serif;
  }
  .letterhead {
    position: absolute; left: 267px; top: 30px;
    width: 665px; height: 940px;
    background: var(--paper);
    box-shadow: 0 6px 24px rgba(80, 30, 55, 0.25);
    overflow: hidden;
  }
  .sidebar {
    position: absolute; left: 0; top: 0;
    width: 141px; height: 100%;
    background: var(--plum);
  }
  .sidebar-stripe {
    position: absolute; left: 141px; top: 0;
    width: 6px; height: 100%;
    background: var(--stripe);
  }
  .sidebar-rule {
    position: absolute; left: 0; top: 248px;
    width: 147px; height: 3px;
    background: var(--paper);
  }
  .contact {
    position: absolute; left: 17px; top: 438px;
    color: var(--sidebar-text);
    font-size: 10.5px; line-height: 18px;
  }
  .contact-heading {
    font-size: 13.5px; font-weight: 400;
    margin-bottom: 14px;
  }
  .location { margin-bottom: 26px; }
  .location .label { display: inline-block; width: 22px; }
  .masthead {
    position: absolute; right: 150px; top: 38px;
    text-align: right;
  }
  .doctor-name {
    font-size: 21px; font-weight: 400;
    color: var(--name-grey); letter-spacing: 0.2px;
  }
  .credentials {
    font-size: 9.5px; color: var(--name-grey);
    letter-spacing: 0.6px; margin-top: 1px;
  }
  .specialty {
    font-size: 16px; font-weight: 600;
    color: var(--plum); margin-top: -1px;
  }
  .brand-dot {
    position: absolute; right: 110px; top: 50px;
    width: 30px; height: 30px; border-radius: 50%;
    background: var(--plum);
  }
  .trace-decoration {
    position: absolute; left: 230px; top: 270px;
    width: 435px; height: 500px;
    background: radial-gradient(ellipse at 60% 50%, var(--trace-tint) 0%, rgba(255,255,255,0) 70%);
  }
</style>
</head>
<body>
  <main class="letterhead">
    <div class="trace-decoration" role="img" aria-label="Faint large heartbeat trace decoration"></div>

    <aside class="sidebar">
      <div class="contact">
        <h2 class="contact-heading">Consulting</h2>
        <div class="location">
          The RB Specialist Centre<br>
          48 Ashcombe Road<br>
          Ashcombe North SA 5021<br>
          <span class="label">T:</span>8312 7740<br>
          <span class="label">F:</span>8312 7741<br>
          Provider No:&nbsp; 518264QT
        </div>
        <div class="location">
          Westgate Cardiology<br>
          &amp; Specialist Clinic<br>
          Linden Central Districts<br>
          Private Hospital<br>
          14-22 Merrow Road<br>
          Fairhaven Vale SA 5118<br>
          <span class="label">T:</span>8356 2090<br>
          <span class="label">F:</span>8356 2091<br>
          <span class="label">E:</span>cardiology@wcsc.com.au<br>
          Provider No:&nbsp; 518264RM
        </div>
        <div class="location">
          Redcliff Bay Hospital<br>
          9 Infirmary Road<br>
          Redcliff Bay 5710<br>
          <span class="label">T:</span>8671 3300<br>
          <span class="label">F:</span>8312 7741<br>
          Provider No:&nbsp; 518264VD
        </div>
      </div>
    </aside>
    <div class="sidebar-stripe"></div>
    <div class="sidebar-rule"></div>

    <header class="masthead">
      <h1 class="doctor-name">Dr&nbsp; Adaeze. O. Marlowe</h1>
      <p class="credentials">M.B.B.S, F.M.C.P, F.R.A.C.P</p>
      <p class="specialty">Cardiologist</p>
    </header>
    <div class="brand-dot"></div>
  </main>
</body>
</html>
```